Brimble Diecast Torvel Collectables Website

looking for a vibrant web site marketplace built for diecast car enthusiasts to buy, sell, and trade with ease. Whether you're looking to showcase your own collection or discover rare and exciting models, our site makes the process simple and enjoyable. Clients can browse a curated inventory of high‑quality diecast cars, connect with fellow collectors, and find the perfect pieces to expand their collection. With a smooth user experience and a community-driven spirit, we’re the go‑to destination for anyone passionate about diecast cars.

Target Market(s)

diecast collectors

Industry/Entity Type

Diecast Collectables

Coding

Coded - Design and coding required

Number of Pages Required

3 page

Font styles to use
Sans Serif

Colors
EE7325
F08F49
F5BC92
FAE3D3
FDF4ED

Requirements
Must have
• Cool look and feel. Woo commerce page to post and sell my inventory
Nice to have
• page for users to post their cars or looking for trades.
Should not have
• look cheap

```html
<!DOCTYPE html>
<html lang="en">
<head>
<meta charset="utf-8">
<title>Brimble Diecast — The Collector's Marketplace for Torvel Diecast</title>
<link rel="stylesheet" href="https://fonts.googleapis.com/css2?family=Anton&family=Inter:wght@400;500;600;700&family=DM+Serif+Text&display=swap">
<style>
:root{
  --orange:#EE7325;--orange-2:#F08F49;--orange-3:#F5BC92;--orange-4:#FAE3D3;--orange-5:#FDF4ED;
  --ink:#151515;--text:#2a2a2a;--muted:#8a8a8a;--line:#e7e5e2;--sand:#f7f5f2;--white:#fff;--dark:#1a1a1a;
}
*{box-sizing:border-box;margin:0;padding:0}
html,body{width:1200px;height:4216px;overflow:hidden}
body{font-family:"Inter",sans-serif;color:var(--text);background:var(--white);font-size:10px}
.wrap{width:810px;margin:0 auto;position:relative}
.display{font-family:"Anton",sans-serif;text-transform:uppercase;color:var(--ink);letter-spacing:.2px;font-weight:400}
.display em{font-style:normal;color:var(--orange)}
.eyebrow{font-size:7.5px;font-weight:600;letter-spacing:2px;text-transform:uppercase;color:var(--orange)}
.photo{border-radius:6px}
.ph-blue{background:radial-gradient(ellipse at 55% 55%,#3a8fe0 0%,#1f3fb0 45%,#17208a 100%)}
.ph-jet{background:linear-gradient(135deg,#2b45b8 0%,#e26a2c 40%,#2a73d8 60%,#1b238c 100%)}
.ph-green{background:radial-gradient(ellipse at 50% 55%,#2f9a4a 0%,#4a5a4c 50%,#8a8f8c 100%)}
.ph-grey{background:radial-gradient(ellipse at 50% 55%,#d9d6d2 0%,#b8b4ae 55%,#e8e6e3 100%)}
.ph-snow{background:linear-gradient(160deg,#6b6a5e 0%,#a8a49a 40%,#d8d4cd 70%,#9a968e 100%)}
.ph-box{background:linear-gradient(135deg,#d9dce6 0%,#2f6fd6 50%,#1e2e8c 100%)}

/* nav */
.nav{height:68px;border-bottom:1px solid var(--line);background:var(--white)}
.nav .wrap{display:flex;align-items:center;height:68px}
.brand{display:flex;align-items:center;gap:8px;font-weight:700;font-size:12px;color:var(--ink)}
.brand-dot{width:22px;height:22px;border-radius:50%;background:var(--orange)}
.nav-links{display:flex;gap:26px;margin-left:auto;margin-right:auto;font-size:9.5px;font-weight:500;color:var(--ink);padding-left:90px}
.nav-right{display:flex;align-items:center;gap:14px;font-size:9.5px;font-weight:600;color:var(--ink)}
.btn{display:inline-flex;align-items:center;gap:6px;border-radius:20px;font-weight:600;font-size:9.5px}
.btn-orange{background:var(--orange);color:#fff}
.btn-ghost{border:1px solid #cfcdca;color:var(--ink);background:#fff}

/* hero */
.hero{height:500px;background:var(--sand)}
.hero .wrap{height:500px}
.tags{position:absolute;top:40px;left:0;display:flex;gap:8px}
.tag{font-size:6.5px;font-weight:700;letter-spacing:1px;padding:4px 7px;border-radius:10px;text-transform:uppercase}
.tag-o{color:var(--orange);background:var(--orange-4)}
.tag-g{color:#555;background:#e9e7e4}
.hero h1{position:absolute;top:72px;left:0;font-size:45px;line-height:49.5px}
.hero-copy{position:absolute;top:292px;left:0;width:300px;font-size:11px;line-height:18.5px;color:#555}
.hero-btns{position:absolute;top:365px;left:0;display:flex;gap:9px}
.hero-btns .btn{height:32px;padding:0 19px}
.proof{position:absolute;top:424px;left:0;display:flex;align-items:center;gap:14px}
.avatars{display:flex}
.avatars span{width:18px;height:18px;border-radius:50%;border:2px solid var(--sand);margin-left:-5px}
.avatars span:first-child{margin-left:0}
.stars{color:var(--orange);font-size:8px;letter-spacing:1px}
.proof small{display:block;font-size:7px;color:var(--muted)}
.proof b{color:var(--ink)}
.hero-photo{position:absolute;right:0;top:153px;width:383px;height:347px;border-radius:6px 6px 0 0}
.listed{position:absolute;left:16px;right:16px;bottom:16px;height:49px;background:rgba(255,255,255,.9);border-radius:8px;display:flex;align-items:center;padding:0 14px;gap:10px}
.listed .ic{width:24px;height:24px;border-radius:6px;background:var(--orange-4);display:flex;align-items:center;justify-content:center}
.listed b{display:block;font-size:9px;color:var(--ink)}
.listed small{font-size:7px;color:var(--muted)}
.listed .price{margin-left:auto;color:var(--orange);font-weight:700;font-size:10px}

/* strip */
.strip{height:41px;background:#faf9f7;border-bottom:1px solid var(--line);display:flex;align-items:center;justify-content:space-between;padding:0 20px;font-size:8px;letter-spacing:2px;font-weight:600;color:#cfccc8;text-transform:uppercase;white-space:nowrap}

/* trending */
.trending{height:517px}
.trending .wrap{padding-top:80px}
.sec-head{display:flex;align-items:flex-end;justify-content:space-between}
.sec-head h2{font-size:23px;line-height:28px;margin-top:8px}
.filters{display:flex;gap:6px}
.filters span{font-size:7.5px;padding:6px 12px;border-radius:12px;background:#efedea;color:#555}
.filters span.on{background:var(--ink);color:#fff}
.cards{display:grid;grid-template-columns:repeat(4,192px);gap:14px;margin-top:22px}
.card{border:1px solid var(--line);border-radius:6px;overflow:hidden;height:226px;background:#fff}
.card .photo{height:144px;border-radius:0;position:relative}
.badge{position:absolute;top:10px;left:10px;font-size:6px;font-weight:700;letter-spacing:1px;padding:3px 6px;border-radius:8px;background:#fff}
.fav{position:absolute;top:9px;right:9px;width:17px;height:17px;border-radius:50%;background:rgba(255,255,255,.85);display:flex;align-items:center;justify-content:center}
.card-body{padding:14px 11px}
.meta{font-size:6.5px;letter-spacing:1px;color:var(--muted);text-transform:uppercase}
.card h3{font-size:9.5px;font-weight:600;color:var(--ink);margin-top:7px}
.card-foot{display:flex;align-items:center;justify-content:space-between;margin-top:15px}
.card-foot b{font-size:13px;color:var(--ink)}
.card-foot small{font-size:7px;color:var(--muted)}
.center{text-align:center}
.view-all{display:flex;justify-content:center;margin-top:30px}
.view-all .btn{height:30px;padding:0 20px}

/* how */
.how{height:410px;background:var(--sand)}
.how .wrap{padding-top:78px;text-align:center}
.how h2,.community h2{font-size:23px;margin-top:9px}
.sub{font-size:9.5px;line-height:14.5px;color:var(--muted);margin:10px auto 0}
.steps{display:grid;grid-template-columns:repeat(3,259px);gap:16px;margin-top:43px;text-align:left}
.step{background:#fff;border:1px solid var(--line);border-radius:8px;height:131px;padding:20px;position:relative}
.icon-box{width:26px;height:26px;border-radius:6px;background:var(--orange-5);display:flex;align-items:center;justify-content:center}
.step .num{position:absolute;top:16px;right:20px;font-family:"DM Serif Text",serif;font-style:italic;font-size:22px;color:#ece9e5}
.step h3{font-size:10px;font-weight:600;color:var(--ink);margin-top:20px}
.step p{font-size:8px;line-height:14px;color:var(--muted);margin-top:8px}

/* why */
.why{height:464px}
.why .wrap{padding-top:75px;display:flex;gap:42px}
.why-photo{width:385px;height:299px;position:relative;flex:none}
.stat-card{position:absolute;left:252px;top:250px;width:110px;height:63px;background:#fff;border-radius:8px;box-shadow:0 8px 24px rgba(0,0,0,.12);padding:13px 14px}
.stat-card b{font-family:"DM Serif Text",serif;font-weight:400;font-size:19px;color:var(--ink);display:block}
.stat-card small{font-size:6.5px;color:var(--muted)}
.why-text{padding-top:16px;width:383px}
.why-text h2{font-size:23px;line-height:34px;margin-top:8px}
.why-text p{font-size:9.5px;line-height:16.5px;color:#666;margin-top:14px}
.checks{list-style:none;margin-top:15px}
.checks li{display:flex;gap:10px;margin-bottom:14px}
.checks b{display:block;font-size:9px;color:var(--ink);font-weight:600}
.checks small{font-size:7.5px;color:var(--muted)}

/* community */
.community{height:763px}
.community .wrap{padding-top:62px;text-align:center}
.community .sub{width:300px}
.stats{background:var(--dark);border-radius:8px;height:126px;margin-top:42px;display:grid;grid-template-columns:repeat(4,1fr);align-items:center}
.stats div{display:flex;flex-direction:column;align-items:center}
.stats .icon-box{background:#2b2b2b}
.stats b{font-family:"DM Serif Text",serif;font-weight:400;color:#fff;font-size:19px;margin-top:12px}
.stats small{font-size:7px;color:#8a8a8a;margin-top:3px}
.quotes{display:grid;grid-template-columns:repeat(3,260px);gap:15px;margin-top:28px;text-align:left}
.quote{border:1px solid var(--line);border-radius:8px;overflow:hidden;height:194px}
.quote .photo{height:106px;border-radius:0;position:relative}
.who{position:absolute;left:10px;bottom:10px;display:flex;align-items:center;gap:7px;color:#fff}
.who span{width:20px;height:20px;border-radius:50%;background:var(--orange);font-size:6.5px;font-weight:700;display:flex;align-items:center;justify-content:center}
.who b{font-size:9px;display:block}
.who small{font-size:6.5px;opacity:.8}
.quote-body{padding:14px}
.quote p{font-size:8px;line-height:14px;color:#555;margin-top:8px}
.perks{display:grid;grid-template-columns:repeat(3,260px);gap:15px;margin-top:26px;text-align:left}
.perk{background:var(--sand);border:1px solid var(--line);border-radius:8px;height:114px;padding:18px}
.perk h3{font-size:9.5px;font-weight:600;color:var(--ink);margin-top:16px}
.perk p{font-size:7.5px;line-height:13px;color:var(--muted);margin-top:6px}

/* gallery */
.gallery{height:724px;background:var(--sand)}
.gallery .wrap{padding-top:75px}
.gallery .sec-head .btn{height:26px;padding:0 14px;font-size:8px}
.grid{display:grid;grid-template-columns:401px 194px 196px;grid-template-rows:146px 146px 146px;column-gap:10px;row-gap:8px;margin-top:25px}
.grid .big{grid-row:1/3}
.gstats{display:flex;justify-content:center;gap:28px;margin-top:22px;align-items:baseline}
.gstats b{font-size:12px;color:var(--ink);margin-right:6px}
.gstats small{font-size:7px;color:var(--muted)}

/* cta */
.cta{height:471px}
.cta .wrap{padding-top:73px}
.cta-box{background:var(--dark);border-radius:10px;height:323px;text-align:center;padding-top:62px}
.cta-box .tag{background:#2e2e2e;color:#bbb}
.cta-box h2{color:#fff;font-size:29px;line-height:44px;margin-top:12px}
.cta-box p{color:#9a9a9a;font-size:9.5px;line-height:16px;width:300px;margin:10px auto 0}
.cta-btns{display:flex;justify-content:center;align-items:center;gap:22px;margin-top:27px}
.cta-btns .btn-orange{height:31px;padding:0 21px}
.cta-btns a{color:#aaa;font-size:9px}

/* footer */
.footer{height:258px;background:#f6f6f7;border-top:1px solid var(--line)}
.footer .wrap{padding-top:48px}
.foot-top{display:grid;grid-template-columns:332px 167px 167px 144px}
.foot-about p{font-size:8px;line-height:14px;color:var(--muted);width:190px;margin-top:18px}
.socials{display:flex;gap:8px;margin-top:14px}
.socials span{width:20px;height:20px;border-radius:50%;background:#e6e6e8;display:flex;align-items:center;justify-content:center}
.foot-col h4{font-size:7px;letter-spacing:1.5px;font-weight:600;color:var(--muted);text-transform:uppercase;margin-top:4px}
.foot-col a{display:block;font-size:8px;color:#555;margin-top:12px;text-decoration:none}
.foot-bottom{display:flex;justify-content:space-between;margin-top:50px;padding-top:12px;font-size:7px;color:var(--muted)}
.foot-bottom nav{display:flex;gap:18px}
</style>
</head>
<body>

<header class="nav">
  <div class="wrap">
    <div class="brand"><span class="brand-dot"></span>Brimble Diecast</div>
    <nav class="nav-links"><span>Browse</span><span>How It Works</span><span>Community</span><span>About</span></nav>
    <div class="nav-right"><span>Sign In</span><span class="btn btn-orange" style="height:24px;padding:0 14px">Start Selling</span></div>
  </div>
</header>

<section class="hero">
  <div class="wrap">
    <div class="tags"><span class="tag tag-o">New Marketplace</span><span class="tag tag-g">2,400+ Listed Models</span></div>
    <h1 class="display">The Collector’s<br><em>Marketplace</em><br>For Torvel<br>Diecast</h1>
    <p class="hero-copy">Buy, sell, and trade premium Torvel diecast models with a vibrant community of collectors. From rare vintage finds to the latest race-day releases.</p>
    <div class="hero-btns">
      <span class="btn btn-orange">Explore Collection
        <svg width="9" height="9" viewBox="0 0 10 10"><path d="M1 5h8M6 2l3 3-3 3" stroke="#fff" stroke-width="1.3" fill="none"/></svg></span>
      <span class="btn btn-ghost">List Your Cars</span>
    </div>
    <div class="proof">
      <div class="avatars"><span style="background:#f2b13a"></span><span style="background:#EE7325"></span><span style="background:#e05a5a"></span><span style="background:#3bb37a"></span><span style="background:#8a6cf0"></span></div>
      <div><div class="stars">★★★★★</div><small>Trusted by <b>8,200+</b> collectors</small></div>
    </div>
    <div class="hero-photo ph-jet" role="img" aria-label="Photo of a rainbow #24 diecast stock car on a blue backdrop">
      <div class="listed">
        <span class="ic"><svg width="12" height="12" viewBox="0 0 12 12"><path d="M6 1l1.5 3.2 3.4.4-2.5 2.3.7 3.4L6 8.6 2.9 10.3l.7-3.4L1.1 4.6l3.4-.4z" fill="none" stroke="#EE7325" stroke-width="1"/></svg></span>
        <div><b>Just Listed</b><small>1:24 Dell Hartley #3 — Mint</small></div>
        <span class="price">$349</span>
      </div>
    </div>
  </div>
</section>

<div class="strip"><span>Lanford Racing</span><span>Apex Replicas</span><span>Pit Crew Models</span><span>Victory Lane Co</span><span>Ravelo</span><span>Quickspin</span><span>Greenflag</span><span>Trackside Authentics</span><span>Oval Club</span><span>Harwick Garage</span></div>

<section class="trending">
  <div class="wrap">
    <div class="sec-head">
      <div><div class="eyebrow">Featured</div><h2 class="display">Trending <em>Right Now</em></h2></div>
      <div class="filters"><span class="on">All</span><span>New Arrivals</span><span>Rare Finds</span><span>Vintage</span></div>
    </div>
    <div class="cards">
      <article class="card">
        <div class="photo ph-box" role="img" aria-label="Photo of a blue #3 diecast car with its display box"><span class="badge" style="color:#3bb37a">Mint</span><span class="fav"><svg width="8" height="8" viewBox="0 0 10 10"><path d="M5 8.5S1 6 1 3.5A2 2 0 0 1 5 2.8 2 2 0 0 1 9 3.5C9 6 5 8.5 5 8.5z" fill="none" stroke="#888" stroke-width="1"/></svg></span></div>
        <div class="card-body"><div class="meta">Apex &nbsp; · &nbsp; 1:24</div><h3>Dell Hartley #3 Wrenchworks</h3><div class="card-foot"><b>$289</b><small>View Details</small></div></div>
      </article>
      <article class="card">
        <div class="photo ph-green" role="img" aria-label="Photo of a green diecast car with open hood"><span class="badge" style="color:#2f7ad8">New</span><span class="fav"><svg width="8" height="8" viewBox="0 0 10 10"><path d="M5 8.5S1 6 1 3.5A2 2 0 0 1 5 2.8 2 2 0 0 1 9 3.5C9 6 5 8.5 5 8.5z" fill="none" stroke="#888" stroke-width="1"/></svg></span></div>
        <div class="card-body"><div class="meta">Lanford &nbsp; · &nbsp; 1:24</div><h3>Jay Garrity #24 Duvant</h3><div class="card-foot"><b>$425</b><small>View Details</small></div></div>
      </article>
      <article class="card">
        <div class="photo ph-blue" role="img" aria-label="Photo of a blue diecast car with open hood"><span class="badge" style="color:var(--orange)">Rare</span><span class="fav"><svg width="8" height="8" viewBox="0 0 10 10"><path d="M5 8.5S1 6 1 3.5A2 2 0 0 1 5 2.8 2 2 0 0 1 9 3.5C9 6 5 8.5 5 8.5z" fill="none" stroke="#888" stroke-width="1"/></svg></span></div>
        <div class="card-body"><div class="meta">Lanford &nbsp; · &nbsp; 1:64</div><h3>Kirk Bastow #18 Candybits</h3><div class="card-foot"><b>$78</b><small>View Details</small></div></div>
      </article>
      <article class="card">
        <div class="photo ph-grey" role="img" aria-label="Photo of a silver and red vintage diecast car"><span class="badge" style="color:#8a6cf0">Vintage</span><span class="fav"><svg width="8" height="8" viewBox="0 0 10 10"><path d="M5 8.5S1 6 1 3.5A2 2 0 0 1 5 2.8 2 2 0 0 1 9 3.5C9 6 5 8.5 5 8.5z" fill="none" stroke="#888" stroke-width="1"/></svg></span></div>
        <div class="card-body"><div class="meta">Apex &nbsp; · &nbsp; 1:24</div><h3>Rowan Pettit #43 Slickoil</h3><div class="card-foot"><b>$356</b><small>View Details</small></div></div>
      </article>
    </div>
    <div class="view-all"><span class="btn btn-ghost">View All Listings
      <svg width="9" height="9" viewBox="0 0 10 10"><path d="M1 5h8M6 2l3 3-3 3" stroke="#151515" stroke-width="1.3" fill="none"/></svg></span></div>
  </div>
</section>

<section class="how">
  <div class="wrap">
    <div class="eyebrow">How It Works</div>
    <h2 class="display">Start Collecting <em>In Minutes</em></h2>
    <p class="sub" style="width:300px">Whether you’re buying your first model or selling a rare find, we’ve made the process dead simple.</p>
    <div class="steps">
      <div class="step"><span class="icon-box"><svg width="11" height="11" viewBox="0 0 12 12"><circle cx="6" cy="4" r="2.2" fill="none" stroke="#EE7325"/><path d="M2 11c0-2.5 1.8-4 4-4s4 1.5 4 4" fill="none" stroke="#EE7325"/></svg></span><span class="num">01</span><h3>Create Your Profile</h3><p>Sign up in seconds and build your collector profile. Showcase your collection and set your preferences.</p></div>
      <div class="step"><span class="icon-box"><svg width="11" height="11" viewBox="0 0 12 12"><circle cx="5" cy="5" r="3.3" fill="none" stroke="#EE7325"/><path d="M7.5 7.5L11 11" stroke="#EE7325"/></svg></span><span class="num">02</span><h3>Browse or List</h3><p>Explore curated listings from collectors worldwide, or photograph and list your own cars in minutes.</p></div>
      <div class="step"><span class="icon-box" style="background:#e4f6ec"><svg width="11" height="11" viewBox="0 0 12 12"><path d="M1 4h9M7.5 1.5L10 4 7.5 6.5M11 8H2M4.5 5.5L2 8l2.5 2.5" fill="none" stroke="#3bb37a"/></svg></span><span class="num">03</span><h3>Buy, Sell or Trade</h3><p>Complete transactions securely with buyer protection. Trade directly with fellow enthusiasts.</p></div>
    </div>
  </div>
</section>

<section class="why">
  <div class="wrap">
    <div class="why-photo photo ph-snow" role="img" aria-label="Photo of a silver and red #29 diecast car outdoors in snow">
      <div class="stat-card"><b>12,480</b><small>Models traded this year</small></div>
    </div>
    <div class="why-text">
      <div class="eyebrow">Why Brimble Diecast</div>
      <h2 class="display">Built By Collectors,<br><em>For Collectors</em></h2>
      <p>We understand the thrill of finding that one rare Torvel model you’ve been chasing. Brimble Diecast was created to bring collectors together in a space that’s as passionate and detail-oriented as the racing world itself.</p>
      <ul class="checks">
        <li><svg width="10" height="10" viewBox="0 0 10 10"><circle cx="5" cy="5" r="5" fill="#FAE3D3"/><path d="M2.8 5.1l1.5 1.5 3-3" stroke="#EE7325" fill="none"/></svg><div><b>Verified Sellers</b><small>Every seller is verified and rated by the community. Shop with confidence.</small></div></li>
        <li><svg width="10" height="10" viewBox="0 0 10 10"><circle cx="5" cy="5" r="5" fill="#FAE3D3"/><path d="M2.8 5.1l1.5 1.5 3-3" stroke="#EE7325" fill="none"/></svg><div><b>Secure Transactions</b><small>Built-in buyer protection with escrow payments on every trade.</small></div></li>
        <li><svg width="10" height="10" viewBox="0 0 10 10"><circle cx="5" cy="5" r="5" fill="#FAE3D3"/><path d="M2.8 5.1l1.5 1.5 3-3" stroke="#EE7325" fill="none"/></svg><div><b>Expert Grading</b><small>Professional condition grading for accurate listings and fair pricing.</small></div></li>
      </ul>
    </div>
  </div>
</section>

<section class="community">
  <div class="wrap">
    <div class="eyebrow">Community</div>
    <h2 class="display">Join The <em>Collector’s Circle</em></h2>
    <p class="sub">More than a marketplace — we’re a passionate community of enthusiasts connecting, sharing, and growing their collections together.</p>
    <div class="stats">
      <div><span class="icon-box"><svg width="11" height="11" viewBox="0 0 12 12"><circle cx="6" cy="4" r="2.2" fill="none" stroke="#EE7325"/><path d="M2 11c0-2.5 1.8-4 4-4s4 1.5 4 4" fill="none" stroke="#EE7325"/></svg></span><b>8,200+</b><small>Active Collectors</small></div>
      <div><span class="icon-box"><svg width="11" height="11" viewBox="0 0 12 12"><rect x="1" y="4" width="10" height="4" rx="1" fill="none" stroke="#EE7325"/><circle cx="3.5" cy="9" r="1" fill="#EE7325"/><circle cx="8.5" cy="9" r="1" fill="#EE7325"/></svg></span><b>24,600+</b><small>Cars Listed</small></div>
      <div><span class="icon-box"><svg width="11" height="11" viewBox="0 0 12 12"><rect x="1" y="2.5" width="10" height="7" rx="1" fill="none" stroke="#EE7325"/><path d="M1 5h10" stroke="#EE7325"/></svg></span><b>$2.4M+</b><small>Total Traded</small></div>
      <div><span class="icon-box"><svg width="11" height="11" viewBox="0 0 12 12"><path d="M6 1l1.5 3.2 3.4.4-2.5 2.3.7 3.4L6 8.6 2.9 10.3l.7-3.4L1.1 4.6l3.4-.4z" fill="none" stroke="#EE7325"/></svg></span><b>4.9/5</b><small>Avg Seller Rating</small></div>
    </div>
    <div class="quotes">
      <div class="quote"><div class="photo ph-green" role="img" aria-label="Photo of a green diecast car from a member collection"><div class="who"><span>MR</span><div><b>Marcus Rivera</b><small>Collector since 2019</small></div></div></div>
        <div class="quote-body"><div class="stars">★★★★★</div><p>“Brimble Diecast completely changed how I collect. I’ve found Torvel models I’ve been searching for years — the community here is incredible.”</p></div></div>
      <div class="quote"><div class="photo ph-blue" role="img" aria-label="Photo of a blue diecast car from a member collection"><div class="who"><span>SC</span><div><b>Sarah Chen</b><small>Top Rated Seller</small></div></div></div>
        <div class="quote-body"><div class="stars">★★★★★</div><p>“I sold my entire duplicate collection in two weeks. The process was smooth, safe, and every buyer was a genuine Torvel enthusiast.”</p></div></div>
      <div class="quote"><div class="photo ph-green" role="img" aria-label="Photo of a green diecast car on a reflective surface"><div class="who"><span>JO</span><div><b>James O’Neill</b><small>1:24 Specialist</small></div></div></div>
        <div class="quote-body"><div class="stars">★★★★★</div><p>“The grading system gives me total confidence in every purchase. No more guessing about condition — everything is transparent.”</p></div></div>
    </div>
    <div class="perks">
      <div class="perk"><span class="icon-box"><svg width="11" height="11" viewBox="0 0 12 12"><path d="M2 3h8v5H5l-3 2z" fill="none" stroke="#EE7325"/></svg></span><h3>Discussion Forums</h3><p>Share tips, ask questions, and connect with collectors who share your passion.</p></div>
      <div class="perk"><span class="icon-box" style="background:#e6f0fb"><svg width="11" height="11" viewBox="0 0 12 12"><rect x="1.5" y="3" width="9" height="6" rx="1.5" fill="none" stroke="#2f7ad8"/></svg></span><h3>Show &amp; Tell Events</h3><p>Monthly virtual meetups where members showcase their latest finds and rarest gems.</p></div>
      <div class="perk"><span class="icon-box" style="background:#e4f6ec"><svg width="11" height="11" viewBox="0 0 12 12"><circle cx="6" cy="4.5" r="3" fill="none" stroke="#3bb37a"/><path d="M4 7l-1 4 3-1.5L9 11 8 7" fill="none" stroke="#3bb37a"/></svg></span><h3>Collector Rewards</h3><p>Earn points on every transaction. Unlock badges, discounts, and exclusive early access.</p></div>
    </div>
  </div>
</section>

<section class="gallery">
  <div class="wrap">
    <div class="sec-head">
      <div><div class="eyebrow">Gallery</div><h2 class="display">From The <em>Showroom Floor</em></h2></div>
      <span class="btn btn-ghost">View All <svg width="8" height="8" viewBox="0 0 10 10"><path d="M1 5h8M6 2l3 3-3 3" stroke="#151515" stroke-width="1.3" fill="none"/></svg></span>
    </div>
    <div class="grid">
      <div class="photo ph-jet big" role="img" aria-label="Photo of a rainbow #24 diecast car on blue backdrop"></div>
      <div class="photo ph-box" role="img" aria-label="Photo of a blue diecast car beside its box"></div>
      <div class="photo ph-green" role="img" aria-label="Photo of a green diecast car with open hood"></div>
      <div class="photo ph-snow" role="img" aria-label="Photo of a silver #29 diecast car in snow"></div>
      <div class="photo ph-grey" role="img" aria-label="Photo of a silver and red diecast car on white"></div>
      <div class="photo ph-blue" role="img" aria-label="Photo of a blue diecast car with open hood" style="grid-column:1"></div>
    </div>
    <div class="gstats"><span><b>2,400+</b><small>Photos Shared</small></span><span><b>340+</b><small>New This Week</small></span><span><b>98%</b><small>Verified Listings</small></span></div>
  </div>
</section>

<section class="cta">
  <div class="wrap">
    <div class="cta-box">
      <span class="tag">Join 8,200+ Collectors</span>
      <h2 class="display">Ready To Find Your<br>Next <em>Race Day Grail</em>?</h2>
      <p>Create your free account and start exploring thousands of premium Torvel diecast models from collectors nationwide.</p>
      <div class="cta-btns"><span class="btn btn-orange">Create Free Account <svg width="9" height="9" viewBox="0 0 10 10"><path d="M1 5h8M6 2l3 3-3 3" stroke="#fff" stroke-width="1.3" fill="none"/></svg></span><a>Browse Listings</a></div>
    </div>
  </div>
</section>

<footer class="footer">
  <div class="wrap">
    <div class="foot-top">
      <div class="foot-about">
        <div class="brand"><span class="brand-dot"></span>Brimble Diecast</div>
        <p>The premier marketplace for Torvel diecast collectors. Buy, sell, and trade with confidence.</p>
        <div class="socials"><span><svg width="8" height="8" viewBox="0 0 10 10"><circle cx="5" cy="5" r="3" fill="#888"/></svg></span><span><svg width="8" height="8" viewBox="0 0 10 10"><rect x="2" y="2" width="6" height="6" fill="#888"/></svg></span></div>
      </div>
      <div class="foot-col"><h4>Marketplace</h4><a>Browse All</a><a>New Arrivals</a><a>Rare Finds</a><a>Sell a Car</a></div>
      <div class="foot-col"><h4>Company</h4><a>About Us</a><a>Community</a><a>Blog</a><a>Careers</a></div>
      <div class="foot-col"><h4>Support</h4><a>Help Center</a><a>Buyer Protection</a><a>Seller Guide</a><a>Contact</a></div>
    </div>
    <div class="foot-bottom"><span>© 2026 Brimble Diecast. All rights reserved.</span><nav><span>Terms</span><span>Privacy</span><span>Cookies</span></nav></div>
  </div>
</footer>

</body>
</html>
```